Real Estate Development Company Web Developer

Hi, I am looking for a website developer to create a website for our new real estate development company. you need to design a website with motion graphics that can be run on any device.
We're looking for sample websites like:
https://larkmontbuild.ca/ or https://www.fennicorehomes.ca/
- The website shall include 6 pages with 1 page hidden.
- The website needs to have 2 versions - English and Chinese
- for your mock-up design, you can use copyright free imagery (we are based in Vancouver, and our projects are townhouses/condos, etc)
Please show examples of professional websites you have done & a mock-up website design for our company. We will shortlist in the next several days and get started straight away. The wording for text content will be detailed in a separate document for each page after we decide the designer.

```html
<!DOCTYPE html>
<html lang="en">
<head>
<meta charset="utf-8">
<title>Northbay Properties Group</title>
<link rel="stylesheet" href="https://fonts.googleapis.com/css2?family=Montserrat:wght@400;500;600;700&display=swap">
<style>
:root{
  --blue:#1f6fbf;
  --dark:#2f2f2f;
  --ink:#222;
  --muted:#8a8a8a;
  --line:#e6e6e6;
  --band:#ececee;
  --white:#fff;
}
*{box-sizing:border-box;margin:0;padding:0}
html,body{width:1200px;height:3094px;overflow:hidden}
body{font-family:'Montserrat',sans-serif;color:var(--ink);background:var(--white);position:relative}
.abs{position:absolute}
.center{left:0;width:1200px;text-align:center}
.eyebrow{font-size:9px;letter-spacing:2.5px;font-weight:500;color:var(--blue)}
.eyebrow::before,.eyebrow::after{content:"";display:inline-block;width:14px;height:1px;background:#ccc;vertical-align:middle;margin:0 8px}
.sec-title{font-size:22px;font-weight:500;letter-spacing:.5px}
.lead{font-size:10px;line-height:16px;color:var(--muted)}

/* hero */
.hero{top:0;left:0;width:1200px;height:590px;background:linear-gradient(90deg,#1c2026 0%,#3a3f46 14%,#5a5e63 35%,#4a4d52 60%,#2a2e34 88%,#15181c 100%)}
.hero::after{content:"";position:absolute;inset:0;background:linear-gradient(180deg,rgba(0,0,0,.2),rgba(0,0,0,.05) 40%,rgba(0,0,0,.3))}
.logo{font-weight:700;font-size:16px;letter-spacing:.5px;display:flex;align-items:center;gap:7px}
.logo small{display:block;font-size:6px;letter-spacing:2px;font-weight:500}
.logo .mark{width:12px;height:12px;background:currentColor}
.nav{top:33px;right:270px;display:flex;gap:18px;font-size:8.5px;font-weight:600;color:var(--white);z-index:2}
.nav .on{color:#5aa6f0;border-bottom:1px solid #5aa6f0;padding-bottom:3px}
.lang{top:33px;left:961px;color:var(--white);font-size:9px;z-index:2}
.join{top:28px;left:995px;width:75px;height:21px;border-radius:11px;background:var(--blue);color:#fff;font-size:8px;font-weight:600;display:flex;align-items:center;justify-content:center;z-index:2}
.hero-copy{top:232px;z-index:2;color:var(--white)}
.hero-copy .kick{font-size:9px;letter-spacing:2.5px;font-weight:500}
.hero-copy h1{font-size:30px;font-weight:500;margin:13px 0 8px}
.hero-copy p{font-size:10.5px;line-height:16px;width:460px;margin:0 auto}
.btn-white{display:inline-block;margin-top:18px;background:#fff;color:#333;font-size:8.5px;letter-spacing:1.5px;padding:9px 17px;border-radius:14px}
.chev{top:544px;left:583px;width:24px;height:24px;border-radius:50%;background:rgba(255,255,255,.2);z-index:2;display:flex;align-items:center;justify-content:center}

/* about */
.about-img{top:653px;left:130px;width:784px;height:392px;background:linear-gradient(180deg,#b9c9d8 0%,#dfe6ee 30%,#8c9aa6 55%,#6f7f8a 70%,#9aa4ab 100%)}
.about-box{top:751px;left:757px;width:313px;height:262px;background:var(--dark);border-right:2px solid var(--blue);padding:40px 38px;color:#fff}
.about-box .k{font-size:8px;letter-spacing:2px;color:var(--blue)}
.about-box h2{font-size:21px;font-weight:600;line-height:28px;margin:10px 0 12px}
.about-box p{font-size:9.5px;line-height:15px;color:#ccc}
.btn-ghost{display:inline-block;margin-top:14px;border:1px solid #ddd;border-radius:12px;font-size:8px;letter-spacing:1.2px;padding:6px 14px;color:#fff}

/* stats */
.stat{top:1096px;width:240px;text-align:center}
.stat .ic{width:58px;height:58px;border-radius:50%;background:var(--dark);margin:0 auto;display:flex;align-items:center;justify-content:center}
.stat.act .ic,.stat.act b{background:var(--blue)}
.stat.act b{background:none;color:var(--blue)}
.stat b{display:block;font-size:25px;font-weight:500;margin:14px 0 6px}
.stat p{font-size:9.5px;line-height:13px;color:var(--muted);width:180px;margin:0 auto}
.rule{top:1293px;left:0;width:1200px;height:1px;background:var(--line)}

/* projects */
.filters{top:1476px;font-size:9px;font-weight:600;letter-spacing:1px}
.filters span{margin:0 6px}
.filters .sep{color:#ccc;font-weight:400}
.filters .on{color:var(--blue)}
.card{top:1532px;width:223px;height:223px;color:#fff;padding:0 19px}
.card h4{position:absolute;bottom:34px;font-size:11px;font-weight:600}
.card p{position:absolute;bottom:20px;font-size:8.5px}
.card .arr{position:absolute;top:22px;left:20px;width:22px;height:22px;border-radius:50%;background:var(--blue);display:flex;align-items:center;justify-content:center}
.btn-blue{top:1781px;left:522px;width:150px;height:27px;border-radius:14px;background:var(--blue);color:#fff;font-size:8.5px;letter-spacing:1.3px;display:flex;align-items:center;justify-content:center;gap:5px}

/* services */
.band{top:1885px;left:0;width:1200px;height:617px;background:var(--band)}
.svc{top:2066px;width:221px;height:352px;color:#fff}
.svc .lbl{position:absolute;bottom:54px;width:100%;text-align:center;font-size:9px;font-weight:700;letter-spacing:1px}
.svc-open{background:var(--dark);text-align:center;padding:28px 26px}
.svc-open h3{font-size:13px;font-weight:600;line-height:19px}
.svc-open p{font-size:9.5px;line-height:15px;color:#ccc;margin-top:10px}
.svc-ic{top:2397px;width:44px;height:44px;border-radius:50%;background:#fff;box-shadow:0 2px 6px rgba(0,0,0,.12);display:flex;align-items:center;justify-content:center}

/* contact band */
.touch{top:2502px;left:0;width:1200px;height:268px;background:linear-gradient(180deg,#4a4d50 0%,#5b5e5e 45%,#3b3a33 75%,#4a3a27 100%)}
.touch-copy{top:2567px;color:#fff}
.touch-copy .k{font-size:8.5px;letter-spacing:2.5px;font-weight:500}
.touch-copy h2{font-size:22px;font-weight:500;margin:8px 0 6px}
.touch-copy p{font-size:10px;line-height:16px;width:460px;margin:0 auto}

/* footer */
.f-logo{top:2840px;left:170px;color:var(--blue)}
.social{top:2888px;left:196px;display:flex;gap:7px}
.social i{width:22px;height:22px;border-radius:50%;border:1px solid var(--line)}
.social i:first-child{background:var(--blue);border-color:var(--blue)}
.fcol{top:2837px;width:150px;font-size:9px;color:var(--muted);line-height:12px}
.fcol h5{font-size:8.5px;font-weight:600;letter-spacing:1px;color:#666}
.fcol h5::after{content:"";display:block;width:18px;height:1px;background:var(--blue);margin:9px 0 10px}
.fcol li{list-style:none;margin-bottom:6px}
.news{top:2919px;left:849px;width:221px;height:26px;border:1px solid var(--line);border-radius:13px;font-size:9px;color:#aaa;padding:7px 15px;display:flex;justify-content:space-between}
.legal{top:3040px;left:130px;width:940px;border-top:1px solid var(--line);padding-top:24px;font-size:8.5px;color:#aaa;display:flex;justify-content:space-between}
.legal span b{font-weight:400;letter-spacing:1px;margin-left:22px}
</style>
</head>
<body>

<div class="abs hero" role="img" aria-label="Dusk view of downtown high-rise towers"></div>
<div class="abs logo" style="top:26px;left:130px;color:#fff;z-index:2"><span class="mark"></span><span>NORTHBAY<small>PROPERTIES GROUP LTD.</small></span></div>
<nav class="abs nav"><span class="on">HOME</span><span>ABOUT US</span><span>OUR SERVICES</span><span>PROJECTS</span><span>CONTACT US</span></nav>
<div class="abs lang">中文</div>
<div class="abs join">
<svg width="9" height="9" viewBox="0 0 10 10" fill="none" stroke="#fff"><circle cx="5" cy="3" r="2"/><path d="M1 9.5c0-2.5 2-3.5 4-3.5s4 1 4 3.5"/></svg>&nbsp;JOIN US</div>
<div class="abs center hero-copy">
  <div class="kick">CREATING OPPORTUNITIES _</div>
  <h1>Lorem Ipsum Is Simply</h1>
  <p>Lorem Ipsum is simply dummy text of the printing and typesetting industry. Lorem Ipsum has been the industry's standard dummy text ever since the 1500s</p>
  <span class="btn-white">EXPLORE MORE</span>
</div>
<div class="abs chev"><svg width="10" height="6" viewBox="0 0 10 6" fill="none" stroke="#fff" stroke-width="1.4"><path d="M1 1l4 4 4-4"/></svg></div>

<div class="abs about-img" role="img" aria-label="Harbour skyline with waterfront and cruise terminal under cloudy sky"></div>
<div class="abs about-box">
  <div class="k">ABOUT &nbsp;—</div>
  <h2>Lorem Ipsum is simply dummy text</h2>
  <p>Lorem Ipsum is simply dummy text of the printing and typesetting industry. Lorem Ipsum has been the industry's standard dummy text ever since the 1500s</p>
  <span class="btn-ghost">MORE ABOUT US</span>
</div>

<div class="abs stat" style="left:120px"><div class="ic"><svg width="24" height="24" viewBox="0 0 24 24" fill="none" stroke="#fff"><circle cx="12" cy="12" r="9"/><ellipse cx="12" cy="12" rx="4" ry="9"/><path d="M3 12h18M5 7h14M5 17h14"/></svg></div><b>5,000</b><p>Lorem Ipsum is simply dummy text of the printing and typesetting</p></div>
<div class="abs stat act" style="left:360px"><div class="ic"><svg width="24" height="24" viewBox="0 0 24 24" fill="none" stroke="#fff"><circle cx="10" cy="10" r="7"/><path d="M15 15l6 6M7 10l2 2 4-4"/></svg></div><b>4,500</b><p>Lorem Ipsum is simply dummy text of the printing and typesetting</p></div>
<div class="abs stat" style="left:600px"><div class="ic"><svg width="24" height="24" viewBox="0 0 24 24" fill="none" stroke="#fff"><circle cx="12" cy="12" r="9"/><circle cx="12" cy="12" r="6"/><circle cx="12" cy="12" r="2"/></svg></div><b>€250M</b><p>Lorem Ipsum is simply dummy text of the printing and typesetting</p></div>
<div class="abs stat" style="left:840px"><div class="ic"><svg width="24" height="24" viewBox="0 0 24 24" fill="none" stroke="#fff"><path d="M3 20h18M6 20V12M10 20V8M14 20V11M18 20V6"/></svg></div><b>2017–18</b><p>Lorem Ipsum is simply dummy text of the printing and typesetting</p></div>

<div class="abs rule"></div>

<div class="abs center" style="top:1358px">
  <div class="eyebrow">PROJECTS</div>
  <h2 class="sec-title" style="margin:14px 0 8px">LOREM IPSUM IS SIMPLY</h2>
  <p class="lead" style="width:460px;margin:0 auto">Lorem Ipsum is simply dummy text of the printing and typesetting industry. Lorem Ipsum has been the industry's standard dummy text ever since the 1500s</p>
</div>
<div class="abs center filters"><span>ALL</span><span class="sep">/</span><span>COMPLETE</span><span class="sep">/</span><span>ONGOING</span><span class="sep">/</span><span class="on">PONTENCIAL</span></div>

<div class="abs card" style="left:135px;background:linear-gradient(180deg,#8f8fb8,#c8c0d0 45%,#6f7480)" role="img" aria-label="Modern white villa with pool at dusk"><h4>1200 ALDER LANE</h4><p>Riverside, BC V5K 0A1, Canada</p></div>
<div class="abs card" style="left:370px;background:linear-gradient(180deg,#4c5f80,#3e5070 60%,#374563)" role="img" aria-label="Modern house with blue overlay"><span class="arr"><svg width="8" height="8" viewBox="0 0 8 8" fill="none" stroke="#fff"><path d="M1 4h6M4 1l3 3-3 3"/></svg></span><h4 style="bottom:40px">1200 ALDER LANE</h4><p style="bottom:26px">Riverside, BC V5K 0A1, Canada</p></div>
<div class="abs card" style="left:605px;background:linear-gradient(180deg,#7e7aa6,#9a8a94 50%,#6b4e44)" role="img" aria-label="Lit two-storey modern house at twilight"><h4>1200 ALDER LANE</h4><p>Riverside, BC V5K 0A1, Canada</p></div>
<div class="abs card" style="left:839px;background:linear-gradient(180deg,#b8bcc4,#8e9288 50%,#5e665c)" role="img" aria-label="Low modern house with lawn and pool"><h4>1200 ALDER LANE</h4><p>Riverside, BC V5K 0A1, Canada</p></div>
<div class="abs btn-blue"><svg width="9" height="9" viewBox="0 0 10 10" fill="none" stroke="#fff"><rect x="1" y="3" width="6" height="6"/><path d="M3 1h6v6"/></svg>VIEW ALL PROJECTS</div>

<div class="abs band"></div>
<div class="abs center" style="top:1950px">
  <div class="eyebrow">SERVICES</div>
  <h2 class="sec-title" style="margin:14px 0 8px">LOREM IPSUM IS SIMPLY</h2>
  <p class="lead" style="width:460px;margin:0 auto">Lorem Ipsum is simply dummy text of the printing and typesetting industry. Lorem Ipsum has been the industry's standard dummy text ever since the 1500s</p>
</div>
<div class="abs svc" style="left:130px;background:linear-gradient(160deg,#5c4a38,#2a2f33 45%,#7a4f30 75%,#2b3035)" role="img" aria-label="Building balconies in warm light"><span class="lbl">SERVICE 1</span></div>
<div class="abs svc" style="left:370px;background:linear-gradient(160deg,#3a3f44,#4b5257 35%,#8a5a36 65%,#2d3236)" role="img" aria-label="Building facade with wooden balconies"><span class="lbl">SERVICE 2</span></div>
<div class="abs svc svc-open" style="left:609px">
  <h3>Lorem Ipsum Is Simply Dummy</h3>
  <p>Lorem Ipsum is simply dummy text of the printing and typesetting industry. Lorem Ipsum has been the industry's standard dummy text ever since the 1500s</p>
  <span class="btn-ghost">LEARN MORE</span>
  <svg class="abs" style="left:103px;top:324px" width="14" height="8" viewBox="0 0 14 8" fill="none" stroke="#1f6fbf"><path d="M1 7l4-4 3 3 5-5"/></svg>
</div>
<div class="abs svc" style="left:849px;background:linear-gradient(160deg,#5a6166,#2b3338 40%,#4c5358 70%,#1f272c)" role="img" aria-label="Dark glass and steel facade"><span class="lbl">SERVICE 4</span></div>
<div class="abs svc-ic" style="left:218px"><svg width="14" height="14" viewBox="0 0 14 14" fill="none" stroke="#555"><path d="M2 3l5-2 5 2v5c0 2-2 4-5 5-3-1-5-3-5-5z"/></svg></div>
<div class="abs svc-ic" style="left:458px"><svg width="14" height="14" viewBox="0 0 14 14" fill="none" stroke="#555"><path d="M2 9a5 5 0 0 1 10 0zM7 9v3"/></svg></div>
<div class="abs svc-ic" style="left:937px"><svg width="14" height="14" viewBox="0 0 14 14" fill="none" stroke="#555"><rect x="1.5" y="1.5" width="11" height="11"/><path d="M4 10V7M7 10V4M10 10V6"/></svg></div>

<div class="abs touch" role="img" aria-label="Misty city skyline and suspension bridge over a forested park"></div>
<div class="abs center touch-copy">
  <div class="k">SUPPORT &nbsp;—</div>
  <h2>GET IN TOUCH</h2>
  <p>Lorem Ipsum is simply dummy text of the printing and typesetting industry. Lorem Ipsum has been the industry's standard dummy text ever since the 1500s</p>
  <span class="btn-white" style="margin-top:22px">&#9711; CREATE ACCOUNT</span>
</div>

<div class="abs logo f-logo" style="font-size:20px"><span class="mark"></span><span>NORTHBAY<small style="font-size:7px">PROPERTIES GROUP LTD.</small></span></div>
<div class="abs social"><i></i><i></i><i></i></div>

<div class="abs fcol" style="left:369px"><h5>LINKS</h5><ul><li>Home</li><li>About Us</li><li>Our Services</li><li>Projects</li><li>Contact Us</li></ul></div>
<div class="abs fcol" style="left:529px"><h5>SERVICES</h5><ul><li>Lorem Ipsum is simply</li><li>Dummy text of the printing Typesetting industry</li><li>Lorem Ipsum has been the industry</li><li>Standard dummy text ever since the 1500s</li></ul></div>
<div class="abs fcol" style="left:689px"><h5>CONTACT</h5><ul><li style="color:#bbb">Address:<br><span style="color:#888">0123 Street, City, State, 10000</span></li><li style="color:#bbb">Phone:<br><span style="color:#888">+012 345 6789</span></li><li style="color:#bbb">Email:<br><span style="color:#888">info@northbayprops.ca</span></li></ul></div>
<div class="abs fcol" style="left:849px;width:221px"><h5>NEWSLETTER</h5><p style="color:#bbb">Subscribe to our emailing list. Lorem Ipsum is simply dummy text of the printing and typesetting industry.</p></div>
<div class="abs news"><span>Your Email Address</span><svg width="11" height="9" viewBox="0 0 11 9" fill="none" stroke="#999"><rect x=".5" y=".5" width="10" height="8"/><path d="M.5 .5l5 4 5-4"/></svg></div>

<div class="abs legal"><span>© Copyright 2022 Northbay Properties Group Ltd. All Rights Reserved</span><span><b>PRIVACY POLICY</b><b>TERMS &amp; CONDITIONS</b></span></div>

</body>
</html>
```